International Clinical Software Company needs a new business card design

We are looking for a new business card design for our company that has recently expanded into the UK market, making us a multinational company.
After having rebranded our website and produced a new style guide, we are looking for a business card that is creative and attention grabbing, while being consistent with the style and colour scheme used on the new website, www.pennick.care
We produce care management technology for the aged care market, but the main aspect we aim to communicate is the human element of our software, and the way it assists in providing better care for aged people, and stronger relationships between aged people and the staff that care for them.
Our current business card is a dark green with gold text, which makes the text quite difficult to read, not very aesthetically appealing and the colour scheme looks quite dated.
We would like something fresh and modern, that can still be colourful but doesn't use large blocks of dark colour, and uses the colours within our logo.
Something tying in with the leaves that are used in our logo could work quite nicely, along with the Autumn/Fall colours of soft greens, yellows and reds (also in our existing logo). However also happy to look at fresh, completely out of the box ideas we may not have yet considered.
Target Market(s)
The people that receive this business card work in the aged card or health industry and are either corporate/management level staff or clinical (Registered Nurses, care workers etc.)
Industry/Entity Type
Health Product
Contact Information for Business Card
Company Name - PennickCare
Company locations: United Kingdom, Australia, New Zealand
Staff Details:
Staff name: Dermot Marlow
Staff job title: Executive Chairman
Staff email: d.marlow@pennick.care
Office phone number: 01632 960481
Other font styles liked:
- Calibri
Requirements
Must have
- Must include the PennickCare brand name in it's current font
- Must include logo (3 leaves in gold circle)
- Must include Business Card Details
Nice to have
- Elements of gold
- White space
- Something autumn themed but not too cliched
Should not have
- No blue - used by a major competitor and we would like to differentiate from them
- Large blocks of dark green colour (the green that appears in our leaves on the logo on our current business card is the background colour and it is far too dark)

```html
<!DOCTYPE html>
<html lang="en">
<head>
<meta charset="utf-8">
<title>PennickCare business card</title>
<link rel="stylesheet" href="https://fonts.googleapis.com/css2?family=Carlito:wght@400;700&display=swap">
<style>
  :root {
    --page: #ecebe6;
    --card: #ffffff;
    --green: #4e8a2b;
    --green-light: #67a23a;
    --yellow: #c8cf3f;
    --gold: #c9c25a;
    --olive: #6f7f18;
    --brand-grey: #c4bca6;
    --white: #ffffff;
  }
  * { margin: 0; padding: 0; box-sizing: border-box; }
  html, body {
    width: 1200px;
    height: 1022px;
    overflow: hidden;
    background: var(--page);
    font-family: "Carlito", "Calibri", sans-serif;
  }
  .business-card {
    position: absolute;
    left: 100px;
    top: 225px;
    width: 1000px;
    height: 572px;
    background: var(--card);
    border-radius: 22px;
    overflow: hidden;
    box-shadow: 0 18px 40px rgba(60, 55, 40, 0.18);
  }
  .card-shapes { position: absolute; inset: 0; }
  .brand {
    position: absolute;
    left: 60px;
    top: 150px;
    display: flex;
    align-items: center;
    gap: 24px;
  }
  .brand-mark {
    width: 140px;
    height: 140px;
    border-radius: 50%;
    border: 5px solid var(--gold);
  }
  .brand-name {
    font-size: 62px;
    font-weight: 400;
    color: var(--brand-grey);
    letter-spacing: 1px;
    white-space: nowrap;
  }
  .contact-list {
    position: absolute;
    left: 70px;
    top: 440px;
    list-style: none;
    color: var(--white);
    font-size: 26px;
    line-height: 40px;
  }
  .contact-list li { display: flex; align-items: center; gap: 14px; }
  .contact-icon { width: 22px; height: 22px; }
  .person {
    position: absolute;
    right: 40px;
    top: 66px;
    text-align: right;
  }
  .person-name {
    font-size: 34px;
    font-weight: 700;
    color: var(--white);
    letter-spacing: 1px;
    text-transform: uppercase;
    line-height: 38px;
  }
  .person-title {
    font-size: 24px;
    color: var(--olive);
    line-height: 30px;
  }
  .locations {
    position: absolute;
    right: 40px;
    top: 192px;
    text-align: right;
    color: var(--white);
    font-size: 26px;
    line-height: 34px;
  }
</style>
</head>
<body>
  <div class="business-card">
    <svg class="card-shapes" width="1000" height="572" viewBox="0 0 1000 572" aria-hidden="true">
      <defs>
        <linearGradient id="greenFill" x1="0" y1="0" x2="0" y2="1">
          <stop offset="0" stop-color="var(--green-light)"/>
          <stop offset="1" stop-color="var(--green)"/>
        </linearGradient>
      </defs>
      <path d="M0,380 L520,380 L660,170 L1000,170 V572 H0 Z" fill="url(#greenFill)"/>
      <path d="M0,366 L508,366 L644,162" fill="none" stroke="var(--gold)" stroke-width="3"/>
      <path d="M640,50 H1000 V150 H720 L700,168 L680,150 H615 Z" fill="var(--yellow)"/>
      <rect x="0" y="552" width="1000" height="20" fill="var(--green)"/>
    </svg>

    <div class="brand">
      <span class="brand-mark"></span>
      <span class="brand-name">PennickCare</span>
    </div>

    <div class="person">
      <p class="person-name">Dermot Marlow</p>
      <p class="person-title">Executive Chairman</p>
    </div>

    <div class="locations">
      <p>United Kingdom</p>
      <p>Australia, New Zealand</p>
    </div>

    <ul class="contact-list">
      <li>
        <svg class="contact-icon" viewBox="0 0 24 24" aria-hidden="true">
          <path d="M6 2 L9 2 L11 7 L8.5 9 C9.5 11.5 12.5 14.5 15 15.5 L17 13 L22 15 L22 18 C22 20 20 22 18 22 C9 21 3 15 2 6 C2 4 4 2 6 2 Z" fill="var(--yellow)"/>
        </svg>
        <span>01632 960481</span>
      </li>
      <li>
        <svg class="contact-icon" viewBox="0 0 24 24" aria-hidden="true">
          <rect x="2" y="5" width="20" height="14" fill="none" stroke="var(--yellow)" stroke-width="2.2"/>
          <path d="M2 5 L12 13 L22 5" fill="none" stroke="var(--yellow)" stroke-width="2.2"/>
        </svg>
        <span>d.marlow@pennick.care</span>
      </li>
    </ul>
  </div>
</body>
</html>
```